Brackwell Removals

We are a domestic removals company, providing the following service:
- removals service
- packing service
- packing materials
- storage facility
- furniture dismantling and reassembling
We would like to start a flyer campaign to customers that just agreed for the house sale.
Our strong key points:
- Good Reviews (Revuemark, Zentrix, shiftquote.com and pagebook)
- Two Men Service (we do all the heavy work for the customer, and place the furniture and boxes to each room of destination)
- Fully Insured
- We can take bookings 7-days of week
- Free and no-obligation survey (we need to do a house visit first in order to provide a fixed and accurate quote)
- Free Quote
Technical Specs:
Landline number: 01632 960418
Contact email: office@brackwellremovals.example.co.uk
Address: Unit 14, Carrow Lane, Northampton NN9 4QT
Website: brackwellremovals.example.co.uk
Took a look on the onto previous projects on FX.com, and liked several flyers already done by you guys, for this industry
We'd like to integrate the colours from our logo in the flyer as well !!

```html
<!DOCTYPE html>
<html lang="en">
<head>
<meta charset="utf-8">
<title>Brackwell Removals – Flyer</title>
<link href="https://fonts.googleapis.com/css2?family=Exo+2:wght@400;500;600;700;800&display=swap" rel="stylesheet">
<style>
  :root{
    --teal:#0f7585;
    --orange:#ff6a13;
    --orange-deep:#f52a10;
    --ink:#2a2a2a;
    --black:#050505;
    --paper:#f6f6f6;
    --rule:#b9b9b9;
    --photo-light:#f3d9b0;
    --photo-dark:#b7834d;
    --white:#ffffff;
  }
  *{box-sizing:border-box;margin:0;padding:0}
  html,body{width:848px;height:1200px;overflow:hidden;background:#e6e6e6}
  body{font-family:"Exo 2",sans-serif;color:var(--ink)}
  .flyer{position:relative;width:848px;height:1200px;background:var(--paper);overflow:hidden}

  .hero{position:absolute;left:0;top:0;width:848px;height:445px}

  .brand{position:absolute;left:0;top:0;width:375px;height:176px;background:var(--white);
    border-radius:0 88px 88px 0;border:4px solid var(--rule);border-left:none;border-top:none;
    display:flex;align-items:center;padding-left:34px}
  .brand-name{font-weight:600;color:var(--ink);font-size:30px;line-height:1.1;letter-spacing:.3px}

  .tab{position:absolute;left:0;background:var(--white);border:4px solid #2f2f2f;border-left:none;
    border-radius:0 26px 26px 0;color:var(--teal);font-weight:700;display:flex;align-items:center}
  .tab-services{top:458px;width:234px;height:48px;padding-left:10px;font-size:20px;letter-spacing:.3px}
  .tab-points{top:700px;width:249px;height:49px;padding-left:6px;font-size:20px;z-index:2}

  .services{position:absolute;top:530px;left:0;width:848px;height:120px}
  .service{position:absolute;top:0;width:170px;margin-left:-85px;text-align:center}
  .service-icon{width:87px;height:87px;margin:0 auto;border-radius:50%;background:radial-gradient(circle at 50% 30%,#3a3a3a,#0a0a0a 70%);
    border:3px solid #222;display:flex;align-items:center;justify-content:center}
  .service-label{margin-top:14px;font-size:15px;font-weight:500;line-height:1.05;color:var(--black)}

  .points{position:absolute;top:700px;left:0;width:848px;height:259px}
  .points-band{position:absolute;inset:0}
  .point-list{position:absolute;list-style:none;color:var(--white);font-size:15.5px;line-height:19.8px;font-weight:500}
  .point-list li{position:relative;padding-left:17px}
  .point-list li::before{content:"";position:absolute;left:0;top:4px;width:8px;height:11px;background:var(--white);
    clip-path:polygon(0 0,45% 0,100% 50%,45% 100%,0 100%,55% 50%)}
  .list-left{left:34px;top:93px;width:410px}
  .list-right{left:464px;top:87px;width:370px}

  .cta{position:absolute;top:968px;left:0;width:848px;text-align:center}
  .cta-title{font-size:32px;font-weight:700;line-height:33px;color:var(--ink);text-transform:uppercase;margin-left:-12px}
  .phone{position:absolute;left:254px;top:1050px;width:319px;height:56px;border:4px solid #2f2f2f;border-radius:28px;
    background:var(--white);display:flex;align-items:center;padding-left:18px;gap:10px;color:var(--teal);font-size:33px;font-weight:500}
  .address{position:absolute;top:1134px;left:326px;width:200px;text-align:center;font-size:15px;font-weight:600;line-height:20px;color:var(--ink);font-style:normal}

  .contact-bar{position:absolute;top:1150px;height:50px;background:var(--black);color:var(--white);font-size:14px;font-weight:600;
    display:flex;align-items:center;justify-content:center;white-space:nowrap}
  .bar-email{left:0;width:307px;border-radius:0 26px 0 0;padding-left:4px}
  .bar-web{left:532px;width:316px;border-radius:26px 0 0 0}
</style>
</head>
<body>
<main class="flyer">

  <svg class="hero" viewBox="0 0 848 445">
    <defs>
      <linearGradient id="photoTone" x1="0" y1="0" x2="1" y2="1">
        <stop offset="0" stop-color="var(--photo-light)"/>
        <stop offset=".55" stop-color="#d9a86e"/>
        <stop offset="1" stop-color="var(--photo-dark)"/>
      </linearGradient>
    </defs>
    <path d="M0,318 C130,380 300,438 398,438 C520,438 700,385 848,332" fill="none" stroke="#9a9a9a" stroke-width="7"/>
    <path role="img" aria-label="Photo of a smiling couple packing cardboard moving boxes in a bright room"
      d="M0,0 H848 V327 C700,378 520,433 398,433 C300,433 130,376 0,312 Z" fill="url(#photoTone)"/>
  </svg>

  <div class="brand">
    <span class="brand-name">Brackwell Removals</span>
  </div>

  <div class="tab tab-services">OUR SERVICES</div>

  <section class="services">
    <div class="service" style="left:90px">
      <div class="service-icon">
        <svg width="52" height="34" viewBox="0 0 52 34"><rect x="0" y="2" width="32" height="22" fill="var(--orange)"/><path d="M34 8h10l7 8v8H34z" fill="var(--orange)"/><rect x="0" y="24" width="51" height="3" fill="var(--orange)"/><circle cx="10" cy="29" r="4.5" fill="var(--orange)" stroke="#111" stroke-width="2"/><circle cx="42" cy="29" r="4.5" fill="var(--orange)" stroke="#111" stroke-width="2"/></svg>
      </div>
      <div class="service-label">removals service</div>
    </div>
    <div class="service" style="left:263px">
      <div class="service-icon">
        <svg width="40" height="50" viewBox="0 0 40 50"><path d="M4 3h8v36" fill="none" stroke="var(--orange)" stroke-width="3"/><rect x="16" y="14" width="18" height="13" fill="var(--orange)"/><rect x="16" y="28" width="22" height="12" fill="var(--orange)"/><path d="M12 42h26" stroke="var(--orange)" stroke-width="3"/><circle cx="12" cy="44" r="4" fill="var(--orange)"/></svg>
      </div>
      <div class="service-label">packing service</div>
    </div>
    <div class="service" style="left:436px">
      <div class="service-icon">
        <svg width="44" height="48" viewBox="0 0 44 48"><ellipse cx="12" cy="36" rx="9" ry="8" fill="none" stroke="var(--orange)" stroke-width="3.5"/><ellipse cx="32" cy="36" rx="9" ry="8" fill="none" stroke="var(--orange)" stroke-width="3.5"/><path d="M10 28 L18 6 H26 L34 28" fill="none" stroke="var(--orange)" stroke-width="3.5"/></svg>
      </div>
      <div class="service-label">packing materials</div>
    </div>
    <div class="service" style="left:599px">
      <div class="service-icon">
        <svg width="50" height="40" viewBox="0 0 50 40"><rect x="17" y="2" width="16" height="16" fill="var(--orange)"/><rect x="3" y="14" width="14" height="22" fill="var(--orange)"/><rect x="17" y="18" width="16" height="18" fill="var(--orange)"/><rect x="33" y="14" width="14" height="22" fill="var(--orange)"/><rect x="0" y="36" width="50" height="3" fill="var(--orange)"/></svg>
      </div>
      <div class="service-label">storage facility</div>
    </div>
    <div class="service" style="left:760px;top:-2px">
      <div class="service-icon">
        <svg width="48" height="46" viewBox="0 0 48 46"><path d="M24 0v12" stroke="var(--orange)" stroke-width="3"/><path d="M18 9l6 7 6-7z" fill="var(--orange)"/><path d="M4 20l20-4 20 4-20 5z" fill="var(--orange)"/><path d="M6 24l18 4v16L6 40z" fill="var(--orange)"/><path d="M42 24l-18 4v16l18-4z" fill="#d9550b"/></svg>
      </div>
      <div class="service-label">furniture dismantling<br>and reassembling</div>
    </div>
  </section>

  <section class="points">
    <svg class="points-band" viewBox="0 0 848 259" preserveAspectRatio="none">
      <defs>
        <linearGradient id="bandTone" x1="0" y1="0" x2="0" y2="1">
          <stop offset="0" stop-color="var(--orange)"/>
          <stop offset="1" stop-color="var(--orange-deep)"/>
        </linearGradient>
      </defs>
      <path d="M0,62 H248 C262,62 262,60 268,40 C276,10 285,0 310,0 H848 V259 H0 Z" fill="url(#bandTone)"/>
    </svg>
    <ul class="point-list list-left">
      <li>Good Reviews (Revuemark, Zentrix, shiftquote.com and pagebook)</li>
      <li>Two Men Service (we do all the heavy work for the customer, and place the furniture and boxes to each room of destination)</li>
      <li>Fully Insured</li>
    </ul>
    <ul class="point-list list-right">
      <li>We can take bookings 7-days of week</li>
      <li>Free and no-obligation survey (we need to do a house visit first in order to provide a fixed and accurate quote)</li>
      <li>Free Quote</li>
    </ul>
  </section>
  <div class="tab tab-points">Our strong key points</div>

  <section class="cta">
    <h1 class="cta-title">Get free quotes<br>today</h1>
  </section>

  <div class="phone">
    <svg width="30" height="30" viewBox="0 0 30 30"><circle cx="15" cy="15" r="13" fill="none" stroke="#2f2f2f" stroke-width="2.5"/><path d="M10 7c-2 1-3 3-2 6 1 4 5 8 9 10 3 1 5 0 6-2l-3-3-2 1c-2-1-4-3-5-5l1-2z" fill="#2f2f2f"/></svg>
    <span>01632 960418</span>
  </div>

  <address class="address">Unit 14, Carrow<br>Lane, Northampton<br>NN9 4QT</address>

  <div class="contact-bar bar-email">office@brackwellremovals.example.co.uk</div>
  <div class="contact-bar bar-web">brackwellremovals.example.co.uk</div>

</main>
</body>
</html>
```